Product label design needed for an odor removal line of products.

I need a label designed for an odor removal product line. There are eight additional odor removal products that I will need labels designed for so the winner will have additional work from me. I would like each of those products to have a similar look and feel in each one. This contest is for one of the products. The Brightwell 417 (would love a better name if you are so inclined -many people know what it is by the 417). The no smell formula does not mask odors, it eliminates odors at their source . Also Reduces Allergens! Simply open silver packet and place in dispenser. Great for use in cars, near pet beds or litter boxes, near diaper pails -anywhere odors are a problem. Lasts 60-90 days. Safe to use. Other uses: Nursing homes, hotel rooms, locker rooms, teenage boy rooms, basements... Eco Friendly! No VOC's or phthalates! Do not consume. Keep out of reach of children and pets. Replace every 60-90 days. I put the picture of my logo , the product as it is packaged and a picture of the actual product and the dispenser it will go in. the package is 4x5 in silver packet with .25 seam on the side and .5 seam on the top and bottom. (Dispenser will have a label with reorder information on it. to be designed later) You do not have to put all information provided on the label. It is to be used as you see fit. I tend to like clean, bold designs but am open to all options. Prefer not to use word air freshener.

Target Market(s)

Men and women between 30-65

Industry/Entity Type

Cleaning Product

Font styles to use
Sans Serif

Colors
acd136
9bcb3c
ffffff

Requirements
Must have
• ability for concept/look to be used for a laundry product, smaller odor elimination pouch, odor removing canister and spray as well
Nice to have
• I like greens but am open to designers to decide
Should not have
• word air freshener

```html
<!DOCTYPE html>
<html lang="en">
<head>
<meta charset="utf-8">
<title>Odor Nixer 417 Label</title>
<link rel="stylesheet" href="https://fonts.googleapis.com/css2?family=Archivo+Black&family=Playfair+Display:ital,wght@1,500&family=Questrial&display=swap">
<style>
  :root {
    --slate: #67686b;
    --leaf: #8dc63f;
    --lime: #9bcb3c;
    --forest: #1e8a3c;
    --white: #ffffff;
  }
  * { margin: 0; padding: 0; box-sizing: border-box; }
  html, body { width: 960px; height: 1200px; overflow: hidden; background: var(--slate); }
  .label { position: relative; width: 960px; height: 1200px; background: var(--slate); }
  .frame {
    position: absolute; left: 64px; top: 264px; width: 835px; height: 880px;
    border: 6px solid var(--leaf); border-radius: 56px;
  }
  .brand-mark {
    position: absolute; left: 344px; top: 128px; width: 272px; height: 272px;
    border-radius: 50%; background: var(--slate);
    display: flex; flex-direction: column; align-items: center; justify-content: center; gap: 18px;
  }
  .brand-dot { width: 96px; height: 96px; border-radius: 50%; background: var(--leaf); }
  .brand-name {
    font-family: "Questrial", sans-serif; font-size: 30px; letter-spacing: 3px;
    color: var(--leaf); text-transform: uppercase; text-align: center; line-height: 1.1;
  }
  .product-kicker {
    position: absolute; left: 0; width: 960px; top: 405px; text-align: center;
    font-family: "Playfair Display", serif; font-style: italic; font-weight: 500;
    font-size: 116px; color: var(--leaf); line-height: 1;
  }
  .product-name {
    position: absolute; left: 0; width: 960px; top: 532px; text-align: center;
    font-family: "Archivo Black", sans-serif; font-size: 142px; line-height: 1;
    color: var(--white); letter-spacing: 2px;
  }
  .product-name .accent { color: var(--forest); }
  .product-number {
    position: absolute; left: 0; width: 960px; top: 660px; text-align: center;
    font-family: "Archivo Black", sans-serif; font-size: 112px; line-height: 1;
    color: var(--lime); transform: scaleX(1.45); letter-spacing: 4px;
  }
  .tagline {
    position: absolute; left: 0; width: 960px; top: 804px; text-align: center;
    font-family: "Questrial", sans-serif; font-size: 36px; letter-spacing: 3px;
    color: var(--white); text-transform: uppercase;
  }
  .bubbles {
    position: absolute; left: 328px; top: 861px; width: 304px; height: 86px;
    border-radius: 43px;
    background: radial-gradient(ellipse at center, var(--forest) 0%, #2f9a45 55%, rgba(103,104,107,0) 100%);
  }
  .badges {
    position: absolute; left: 0; width: 960px; top: 960px;
    display: flex; justify-content: center; gap: 3px;
  }
  .badge {
    width: 96px; height: 96px; border-radius: 50%; background: var(--leaf);
    display: flex; flex-direction: column; align-items: center; justify-content: center;
    font-family: "Questrial", sans-serif; color: var(--white); text-transform: uppercase;
    font-size: 12px; letter-spacing: 1px; line-height: 1.1; text-align: center; font-weight: bold;
  }
  .badge svg { width: 34px; height: 34px; margin: 3px 0; }
</style>
</head>
<body>
  <main class="label">
    <div class="frame"></div>

    <div class="brand-mark">
      <span class="brand-dot"></span>
      <span class="brand-name">Verdale Home</span>
    </div>

    <p class="product-kicker">Odor</p>
    <h1 class="product-name">NI<span class="accent">X</span>ER</h1>
    <p class="product-number">417</p>
    <p class="tagline">Eliminates tough odors</p>

    <div class="bubbles" role="img" aria-label="Cluster of green bubbles"></div>

    <ul class="badges">
      <li class="badge">
        <span>100%</span>
        <svg viewBox="0 0 34 34" aria-hidden="true"><path d="M17 30 C17 20 22 12 30 8 C28 18 24 24 17 30 Z M17 30 C15 22 10 16 4 14 C6 22 10 27 17 30 Z" fill="#ffffff"/></svg>
        <span>Natural</span>
      </li>
      <li class="badge">
        <span>Odor</span>
        <svg viewBox="0 0 34 34" aria-hidden="true"><path d="M9 28 C5 22 13 18 9 8 M17 28 C13 22 21 18 17 8 M25 28 C21 22 29 18 25 8" fill="none" stroke="#ffffff" stroke-width="3" stroke-linecap="round"/></svg>
        <span>Free</span>
      </li>
      <li class="badge">
        <span>For all</span>
        <svg viewBox="0 0 34 34" aria-hidden="true"><rect x="8" y="4" width="18" height="26" rx="2" fill="none" stroke="#ffffff" stroke-width="3"/><line x1="8" y1="13" x2="26" y2="13" stroke="#ffffff" stroke-width="3"/></svg>
        <span>Rooms</span>
      </li>
    </ul>
  </main>
</body>
</html>
```